依頼概要
▽ターゲット
【■ 40~80歳■】向けの【■ ふとんの打ち直し■】販促用にポスターデザインを作成したいと考えており、デザイナー・クリエイターの方向けにコンペを開催いたします。

▽サイズ
【■A2サイズでトンボを付けて下さい。そのまま印刷屋に出せる形式(AIファイル必須■】

▽参考デザイン
サイト名:【■ ねむり堂川 ■】
参考URL:【■ http://www.nemuridokawa.co.jp/SHOP/582716/list.html■】

```html
<!DOCTYPE html>
<html lang="ja">
<head>
<meta charset="utf-8">
<title>お布団の打ち直し</title>
<link href="https://fonts.googleapis.com/css2?family=M+PLUS+Rounded+1c:wght@400;700;800&display=swap" rel="stylesheet">
<style>
:root{
  --cream:#fdf7e6;
  --pink:#e8588a;
  --brown:#6b4a36;
  --yellow:#fbe27a;
  --green:#5a9a3c;
  --ink:#3d3029;
  --white:#ffffff;
}
*{margin:0;padding:0;box-sizing:border-box}
html,body{width:846px;height:1200px;overflow:hidden}
body{background:var(--cream);font-family:"M PLUS Rounded 1c",sans-serif;color:var(--ink);position:relative}
.title{position:absolute;top:22px;left:0;width:100%;text-align:center;font-size:60px;font-weight:800;color:var(--pink);letter-spacing:4px}
.lead{position:absolute;top:104px;left:0;width:100%;text-align:center;font-size:15px;font-weight:700}
.lead em{font-style:normal;color:var(--green)}
.panel{position:absolute;width:384px;height:282px;background:var(--white);border:3px solid var(--brown);border-radius:14px;overflow:hidden}
.p1{left:432px;top:140px}.p2{left:30px;top:140px}.p3{left:432px;top:436px}.p4{left:30px;top:436px}
.num{position:absolute;top:8px;right:8px;width:34px;height:34px;border-radius:50%;background:var(--brown);color:var(--white);font-weight:800;font-size:20px;text-align:center;line-height:34px;z-index:2}
.illus{position:absolute;border-radius:10px}
.p1 .illus{left:14px;top:50px;width:150px;height:218px;background:linear-gradient(#fbe6d4,#f5c6a8)}
.p2 .illus{left:14px;top:14px;width:356px;height:254px;background:linear-gradient(#f3ece0,#e4d8c4)}
.p3 .illus{left:220px;top:50px;width:150px;height:218px;background:linear-gradient(#f7c9d6,#e88aa5)}
.p4 .illus{left:14px;top:14px;width:356px;height:254px;background:linear-gradient(#fbe0e8,#d9c8f0)}
.ptext{position:absolute;z-index:2;font-weight:700;line-height:1.5}
.p1 .ptext{left:178px;top:60px;font-size:15px}
.p1 .big{display:block;font-size:25px;color:var(--pink);font-weight:800;line-height:1.3;margin-top:8px}
.tag{position:absolute;z-index:2;background:var(--white);border:2px solid var(--brown);border-radius:8px;padding:4px 8px;font-size:15px;font-weight:700}
.tag b{color:var(--pink)}
.p3 .ptext{left:18px;top:56px;font-size:15px}
.p3 .hl{background:var(--pink);color:var(--white);padding:0 4px}
.p3 .shop{color:var(--pink);font-size:20px;font-weight:800}
.p4 .ptext{left:36px;top:40px;font-size:15px;background:rgba(255,255,255,.9);padding:8px 12px;border-radius:10px}
.p4 .big{display:block;color:var(--pink);font-size:24px;font-weight:800}
.campaign{position:absolute;left:28px;bottom:18px;z-index:2;width:90px;height:90px;border-radius:50%;background:var(--yellow);border:2px solid var(--pink);text-align:center;font-weight:800;font-size:13px;color:var(--pink);padding-top:24px;line-height:1.4}
.desc{position:absolute;top:744px;left:430px;width:390px;font-size:15px;font-weight:700;line-height:1.75}
.desc em{font-style:normal;color:var(--pink);border-bottom:2px solid var(--pink)}
.prices{position:absolute;top:818px;left:36px;width:370px}
.row{display:flex;justify-content:space-between;align-items:baseline;border-bottom:2px dotted var(--brown);padding:4px 0}
.row .size{font-size:26px;font-weight:800}
.row .yen{font-size:32px;font-weight:800;color:var(--pink)}
.row .yen small{font-size:20px}
.note{position:absolute;top:1000px;left:36px;font-size:10px}
.info{position:absolute;left:430px;width:390px;border:2px solid var(--pink);background:var(--white);font-size:10px;line-height:1.6;padding:4px 8px 6px}
.info h3{font-size:12px;color:var(--pink);font-weight:800}
.i1{top:830px}.i2{top:922px}
.footer{position:absolute;top:1060px;left:30px;right:30px;border-top:3px solid var(--pink);padding-top:26px;display:flex;justify-content:space-between;align-items:center}
.ask{font-size:22px;font-weight:800}
.brand{display:flex;align-items:center;gap:10px;font-size:32px;font-weight:800;color:var(--ink)}
.brand-dot{width:18px;height:18px;border-radius:50%;background:var(--pink)}
</style>
</head>
<body>
<h1 class="title">お布団の打ち直し</h1>
<p class="lead">長年使った綿わたのお布団は、打ち直しで<em>リフレッシュ</em>することができます</p>

<section class="panel p1">
  <div class="num">1</div>
  <div class="illus" role="img" aria-label="布団を干す女性のイラスト"></div>
  <p class="ptext">最近、お布団を干しても<br>以前のように<span class="big">ふっくらしなく<br>なったな…</span></p>
</section>

<section class="panel p2">
  <div class="num">2</div>
  <div class="illus" role="img" aria-label="傷んだ布団を抱える女性のイラスト"></div>
  <p class="tag" style="left:40px;top:30px">生地が<b>破れ</b>た<br>お布団</p>
  <p class="tag" style="left:190px;top:20px"><b>汚れ</b>たお布団</p>
  <p class="tag" style="left:250px;top:110px"><b>つぶれ</b>た<br>お布団</p>
  <p class="tag" style="left:40px;top:120px">汗を<b>吸わなく</b><br>なったお布団</p>
</section>

<section class="panel p3">
  <div class="num">3</div>
  <div class="illus" role="img" aria-label="打ち直し前後の布団のイラスト"></div>
  <p class="ptext">綿わたのお布団は<br><span class="hl">打ち直し</span>ができるから<br><span class="shop">やすらぎ寝具店</span><br>におまかせ</p>
  <p class="tag" style="left:230px;top:200px">ふかふかに<br><b>リフレッシュ</b></p>
</section>

<section class="panel p4">
  <div class="num">4</div>
  <div class="illus" role="img" aria-label="ぐっすり眠る家族のイラスト"></div>
  <p class="ptext">新品同様の仕上がりなら<span class="big">快眠をお約束</span></p>
  <div class="campaign">今なら<br>キャンペーン中</div>
</section>

<p class="desc">古くなったお布団の<em>中わたをほぐし</em>、外側を<em>新しい生地に交換</em>して新品同様に蘇り直します。</p>

<div class="prices">
  <div class="row"><span class="size">シングル</span><span class="yen">8,800<small>円～</small></span></div>
  <div class="row"><span class="size">セミダブル</span><span class="yen">9,800<small>円～</small></span></div>
  <div class="row"><span class="size">ダブル</span><span class="yen">10,800<small>円～</small></span></div>
</div>
<p class="note">※表示価格は税込です。生地・綿の量により料金が異なります。</p>

<div class="info i1">
  <h3>新品の詳細について</h3>
  <p>●中わたは国内で丁寧にほぐし、不純物を取り除きます。<br>●生地は綿100％の新しいものに交換いたします。<br>●仕上がりまでの期間は約二週間です。</p>
</div>
<div class="info i2">
  <h3>仕立て直し・新品共通の詳細について</h3>
  <p>●お引き取り・お届けも承ります。お気軽にご相談ください。<br>●詳しい料金は店頭にてお見積りいたします。</p>
</div>

<footer class="footer">
  <p class="ask">詳しくは店内にてお気軽にご相談ください。</p>
  <p class="brand"><span class="brand-dot"></span>やすらぎ寝具店</p>
</footer>
</body>
</html>
```